Bright Hall Meetings: Educators and Families joining forces for pupil growth.

This is a book that helps to prepare for and hold a standard conference that an educator would have with the parents of the students in the school. It is also about how to have problem-solving conferences around difficult issues using techniques from family therapy. Parent involvement is a key ingredient for student success, but most educators have no training in holding meetings with parents. This book fills that gap.
Updates

Need extra days to review

Target Market(s)

Teachers, principals, counselors, school psychologists, school nurses. Anyone who has conferences with the parents of their students.

Font styles to use
Sans Serif

Colors
85acd3
ffcf3e

Requirements
Must have
• I have several books coming up. I'd like something that could be carried over to the new ones without too many changes. They won't all be about education. I am a psychologist so most of my writings will cover subjects related to emotional intelligence.
Nice to have
• Something dignified that will pop out for those in the schools. I like the combination of a royal blue background with white and gold (not yellow) lettering.
Should not have
• I'd like it to be easy to read. Not too messy or too much stuff on the page.

```html
<!DOCTYPE html>
<html lang="en">
<head>
<meta charset="utf-8">
<title>Bright Hall Meetings – Book Cover</title>
<link rel="stylesheet" href="https://fonts.googleapis.com/css2?family=Bebas+Neue&family=Mulish:wght@500&display=swap">
<style>
  :root {
    --page-bg: #ececec;
    --royal-deep: #060a7e;
    --royal-light: #1c2796;
    --gold-light: #f7dc8a;
    --gold-mid: #d9ac45;
    --gold-dark: #a9781f;
    --ink-white: #ffffff;
  }
  * { margin: 0; padding: 0; box-sizing: border-box; }
  html, body {
    width: 1200px;
    height: 897px;
    overflow: hidden;
    background: var(--page-bg);
  }
  .stage {
    position: relative;
    width: 1200px;
    height: 897px;
    display: flex;
    align-items: center;
    justify-content: center;
  }
  .book-cover {
    position: relative;
    width: 558px;
    height: 837px;
    background: radial-gradient(ellipse at 20% 10%, var(--royal-light) 0%, var(--royal-deep) 60%, #05087a 100%);
    box-shadow: 0 10px 30px rgba(0, 0, 0, 0.18);
  }
  .cover-title {
    position: absolute;
    left: 0;
    top: 0;
    width: 558px;
    height: 460px;
  }
  .cover-title text {
    font-family: "Bebas Neue", "Oswald", sans-serif;
    fill: url(#gold-foil);
  }
  .cover-subtitle {
    position: absolute;
    left: 0;
    right: 0;
    top: 472px;
    text-align: center;
    font-family: "Mulish", sans-serif;
    font-weight: 500;
    font-size: 28px;
    line-height: 35px;
    color: var(--ink-white);
    letter-spacing: 0.2px;
  }
</style>
</head>
<body>
<main class="stage">
  <article class="book-cover">
    <svg class="cover-title" viewBox="0 0 558 460" role="heading" aria-level="1" aria-label="Bright Hall Meetings">
      <defs>
        <linearGradient id="gold-foil" x1="0" y1="0" x2="1" y2="1">
          <stop offset="0" stop-color="var(--gold-light)"/>
          <stop offset="0.35" stop-color="var(--gold-mid)"/>
          <stop offset="0.55" stop-color="var(--gold-light)"/>
          <stop offset="0.8" stop-color="var(--gold-dark)"/>
          <stop offset="1" stop-color="var(--gold-mid)"/>
        </linearGradient>
      </defs>
      <text x="84" y="221" font-size="149" textLength="392" lengthAdjust="spacingAndGlyphs">BRIGHT</text>
      <text x="84" y="349" font-size="172" textLength="392" lengthAdjust="spacingAndGlyphs">HALL</text>
      <text x="84" y="429" font-size="103" textLength="392" lengthAdjust="spacingAndGlyphs">MEETINGS</text>
    </svg>
    <p class="cover-subtitle">Educators and Families<br>joining forces<br>for pupil growth</p>
  </article>
</main>
</body>
</html>
```